Cedar Hollow responsive web design

We need a responsive, bootstrap compatible (but design only - PSD files) website design for a fly fishing shop and guide service.

Design should be very clean. Home Page design + interior page design please.

Possible Home Page Content:
Slide Show
Highlight Three Features: Guided Trips, Fly Shop, Missouri River
About

Thank you and good luck!

Shop

• This will be used on Bootstrap CMS so needs 12 column bootstrap measurements.

DESIGN ONLY NEEDED (clean PSD files), no programming required.
Need a Home Page layout and secondary page layout

Must show use of the following:
H1 - H5 font uses
link color
Dropdown for navigation bar
Button example
• No cutout images, this will be part of CMS and client needs to be able to update most content without knowing photoshop.

```html
<!DOCTYPE html>
<html lang="en">
<head>
<meta charset="utf-8">
<title>Cedar Hollow – Fly Shop &amp; Guide Service</title>
<link rel="stylesheet" href="https://fonts.googleapis.com/css2?family=Open+Sans:wght@300;400;600;700&display=swap">
<style>
  :root{
    --blue:#1e9bd7;
    --blue-dark:#1579b0;
    --ink:#333b40;
    --muted:#6b7378;
    --rule:#d9dee1;
    --white:#ffffff;
    --footer:#2b2f33;
    --hero-a:#6f7d86;
    --hero-b:#b9a48a;
    --hero-c:#3f4a40;
  }
  *{box-sizing:border-box;margin:0;padding:0}
  html,body{width:758px;height:1200px;overflow:hidden}
  body{position:relative;background:var(--white);font-family:"Open Sans",Arial,sans-serif;color:var(--ink)}

  /* header */
  .site-header{position:absolute;left:0;top:0;width:758px;height:96px;background:var(--white)}
  .brand{position:absolute;left:70px;top:20px;display:flex;align-items:center;gap:8px}
  .brand-mark{width:22px;height:22px;background:var(--blue)}
  .brand-name{font-size:22px;font-weight:700;color:var(--blue);letter-spacing:.2px}
  .search{position:absolute;left:500px;top:20px;width:164px;height:24px;display:flex;border:1px solid var(--rule)}
  .search input{flex:1;border:0;font:400 9px "Open Sans",sans-serif;padding:0 8px;color:var(--muted)}
  .search button{width:24px;border:0;background:var(--blue);display:flex;align-items:center;justify-content:center}
  .main-nav{position:absolute;right:94px;top:66px;display:flex;gap:22px;font-size:10px;font-weight:600;color:var(--ink)}
  .main-nav .caret{font-size:7px;margin-left:3px;color:var(--muted)}

  /* hero */
  .hero{position:absolute;left:0;top:96px;width:758px;height:336px;overflow:hidden}
  .hero-photo{position:absolute;inset:0;background:linear-gradient(100deg,var(--hero-a) 0%,var(--hero-b) 45%,var(--hero-a) 70%,var(--hero-c) 100%)}
  .hero-copy{position:absolute;left:72px;top:108px;color:var(--white)}
  .hero-copy h1{font-size:40px;font-weight:300;line-height:1.1}
  .hero-copy h1 strong{font-weight:600}
  .hero-copy p{font-size:17px;font-weight:400;line-height:1.25;margin-top:8px;width:420px}
  .btn{display:inline-block;margin-top:18px;background:var(--blue);color:var(--white);font-size:12px;padding:8px 22px;text-decoration:none}
  .slider-dots{position:absolute;left:382px;top:308px;display:flex;gap:6px}
  .slider-dots span{width:7px;height:7px;border-radius:50%;background:rgba(255,255,255,.55)}
  .slider-dots span.active{background:var(--white)}

  /* section headings */
  .section-title{position:absolute;display:flex;align-items:center;gap:14px;font-weight:300;color:var(--ink)}
  .section-title .line{height:1px;background:var(--rule)}
  .title-welcome{left:0;width:758px;top:462px;justify-content:center;font-size:30px}
  .title-welcome .line{width:58px;background:var(--blue)}
  .title-left{left:70px;width:618px;font-size:26px}
  .title-left .line{flex:1}
  .title-left .tag{width:30px;height:2px;background:var(--blue)}

  /* feature icons */
  .highlights{position:absolute;left:70px;top:522px;width:618px;display:flex;justify-content:space-between}
  .highlight{width:180px;text-align:center}
  .highlight svg{display:block;margin:0 auto 10px}
  .highlight h3{font-size:13px;font-weight:600;margin-bottom:6px}
  .highlight p{font-size:10px;line-height:1.4;color:var(--muted)}

  /* cards */
  .features{position:absolute;left:70px;top:744px;width:618px;display:flex;justify-content:space-between}
  .feature-card{width:188px}
  .feature-photo{height:110px;margin-bottom:10px}
  .photo-a{background:linear-gradient(160deg,#c88b3a,#7a6a3d 60%,#3d4a3a)}
  .photo-b{background:linear-gradient(180deg,#8fb7c4,#4e7a86 55%,#2f5560)}
  .photo-c{background:linear-gradient(180deg,#9cb7cf,#8a7b63 55%,#4f5b45)}
  .feature-card h4{font-size:12px;font-weight:600}
  .feature-card p{font-size:10px;line-height:1.4;color:var(--muted);margin-top:3px}

  /* services */
  .services-text{position:absolute;left:70px;top:990px;width:300px}
  .services-text p{font-size:10px;line-height:1.5;color:var(--muted)}
  .check-list{list-style:none;display:grid;grid-template-columns:1fr 1fr;gap:9px 12px;margin-top:16px}
  .check-list li{font-size:10px;color:var(--muted);display:flex;align-items:center;gap:6px}
  .services-photo{position:absolute;left:396px;top:994px;width:134px;height:102px;background:linear-gradient(180deg,#9cc0cf,#5f8c7a 60%,#3c5a48)}
  .services-links{position:absolute;left:530px;top:972px}
  .thumb{position:absolute;width:50px;height:50px;border-radius:50%;border:2px solid var(--white);box-shadow:0 0 0 1px var(--rule)}
  .thumb-1{left:96px;top:0;background:linear-gradient(160deg,#7a8a8f,#3f4d4a)}
  .thumb-2{left:96px;top:56px;background:linear-gradient(160deg,#6d98b0,#2f566a)}
  .thumb-3{left:96px;top:112px;background:linear-gradient(160deg,#b58a5c,#5b4a36)}

  /* footer */
  .site-footer{position:absolute;left:0;top:1172px;width:758px;height:28px;background:var(--footer);color:#c8ccce;font-size:9px;display:flex;align-items:center;justify-content:center}
</style>
</head>
<body>

<header class="site-header">
  <div class="brand"><span class="brand-mark"></span><span class="brand-name">Cedar Hollow</span></div>
  <form class="search">
    <input type="text" value="Search entire store here...">
    <button type="button" aria-label="Search">
      <svg width="11" height="11" viewBox="0 0 12 12"><circle cx="5" cy="5" r="3.6" fill="none" stroke="#fff" stroke-width="1.6"/><line x1="7.6" y1="7.6" x2="11" y2="11" stroke="#fff" stroke-width="1.6"/></svg>
    </button>
  </form>
  <nav class="main-nav">
    <span>HOME</span>
    <span>FLY SHOP<span class="caret">▼</span></span>
    <span>GUIDE SERVICE<span class="caret">▼</span></span>
    <span>MISSOURI RIVER<span class="caret">▼</span></span>
    <span>CONTACT</span>
  </nav>
</header>

<section class="hero">
  <div class="hero-photo" role="img" aria-label="Angler holding a fly rod beside a misty river at dawn"></div>
  <div class="hero-copy">
    <h1>Cedar <strong>Hollow</strong></h1>
    <p>Lorem ipsum dolor sit amet, consectetur adipisicing elit, sed do eiusmod tempor incid</p>
    <a class="btn" href="#">Read More</a>
  </div>
  <div class="slider-dots"><span class="active"></span><span></span><span></span></div>
</section>

<h2 class="section-title title-welcome"><span class="line"></span>Welcome To Cedar Hollow<span class="line"></span></h2>

<div class="highlights">
  <div class="highlight">
    <svg width="52" height="52" viewBox="0 0 52 52"><rect x="2" y="2" width="48" height="48" rx="8" fill="none" stroke="var(--blue)" stroke-width="3"/><path d="M14 36 L14 18 L22 14 L30 18 L38 14 L38 32 L30 36 L22 32 Z" fill="none" stroke="var(--blue)" stroke-width="2.5" stroke-linejoin="round"/><line x1="22" y1="14" x2="22" y2="32" stroke="var(--blue)" stroke-width="2"/><line x1="30" y1="18" x2="30" y2="36" stroke="var(--blue)" stroke-width="2"/></svg>
    <h3>Guided Trips</h3>
    <p>Lorem Ipsum is simply dummy text of the printing and typesetting industry.</p>
  </div>
  <div class="highlight">
    <svg width="52" height="52" viewBox="0 0 52 52"><path d="M8 20 L12 8 L40 8 L44 20 Z" fill="var(--blue)"/><path d="M8 20 q4.5 6 9 0 q4.5 6 9 0 q4.5 6 9 0 q4.5 6 9 0" fill="none" stroke="var(--blue)" stroke-width="2.5"/><rect x="11" y="26" width="30" height="20" fill="none" stroke="var(--blue)" stroke-width="3"/><rect x="16" y="31" width="9" height="15" fill="var(--blue)"/><rect x="29" y="31" width="8" height="7" fill="var(--blue)"/></svg>
    <h3>Fly Shop</h3>
    <p>Lorem Ipsum is simply dummy text of the printing and typesetting industry.</p>
  </div>
  <div class="highlight">
    <svg width="52" height="52" viewBox="0 0 52 52"><path d="M26 6 L26 34 L10 34 Z" fill="var(--blue)"/><path d="M29 12 L42 34 L29 34 Z" fill="var(--blue)"/><path d="M6 38 L46 38 L40 46 L12 46 Z" fill="var(--blue)"/></svg>
    <h3>Missouri River</h3>
    <p>Lorem Ipsum is simply dummy text of the printing and typesetting industry.</p>
  </div>
</div>

<h2 class="section-title title-left" style="top:694px"><span class="tag"></span>Features Cedar Hollow<span class="line"></span></h2>

<div class="features">
  <article class="feature-card">
    <div class="feature-photo photo-a" role="img" aria-label="River bank under autumn trees"></div>
    <h4>Guided Trips</h4>
    <p>Lorem Ipsum is simply dummy text of the printing and typesetting industry. Lorem Ipsum has been the industry's standard</p>
  </article>
  <article class="feature-card">
    <div class="feature-photo photo-b" role="img" aria-label="Drift boat on calm blue water"></div>
    <h4>Guided Trips</h4>
    <p>Lorem Ipsum is simply dummy text of the printing and typesetting industry. Lorem Ipsum has been the industry's standard</p>
  </article>
  <article class="feature-card">
    <div class="feature-photo photo-c" role="img" aria-label="Fly shop building with parking lot"></div>
    <h4>Guided Trips</h4>
    <p>Lorem Ipsum is simply dummy text of the printing and typesetting industry. Lorem Ipsum has been the industry's standard</p>
  </article>
</div>

<h2 class="section-title title-left" style="top:944px"><span class="tag"></span>Features Services<span class="line"></span></h2>

<div class="services-text">
  <p>Rutrum vel sem nunc dolor in hendrerit in vulputate velit esse molestie consequat, vel illum dolore eu feugiat nulla.</p>
  <ul class="check-list">
    <li><svg width="9" height="9" viewBox="0 0 10 10"><path d="M1 5 L4 8 L9 2" fill="none" stroke="var(--blue)" stroke-width="1.8"/></svg>Easy to cast rods</li>
    <li><svg width="9" height="9" viewBox="0 0 10 10"><path d="M1 5 L4 8 L9 2" fill="none" stroke="var(--blue)" stroke-width="1.8"/></svg>Best support all days</li>
    <li><svg width="9" height="9" viewBox="0 0 10 10"><path d="M1 5 L4 8 L9 2" fill="none" stroke="var(--blue)" stroke-width="1.8"/></svg>Fast effective guide team</li>
    <li><svg width="9" height="9" viewBox="0 0 10 10"><path d="M1 5 L4 8 L9 2" fill="none" stroke="var(--blue)" stroke-width="1.8"/></svg>Patient guides on water</li>
    <li><svg width="9" height="9" viewBox="0 0 10 10"><path d="M1 5 L4 8 L9 2" fill="none" stroke="var(--blue)" stroke-width="1.8"/></svg>Open daily for anglers</li>
    <li><svg width="9" height="9" viewBox="0 0 10 10"><path d="M1 5 L4 8 L9 2" fill="none" stroke="var(--blue)" stroke-width="1.8"/></svg>Quality tackle every season</li>
  </ul>
</div>

<div class="services-photo" role="img" aria-label="Anglers in a boat on a wide river"></div>
<div class="services-links">
  <svg width="100" height="170" viewBox="0 0 100 170" style="position:absolute;left:0;top:0">
    <g stroke="var(--blue)" stroke-width="1.2" fill="none">
      <line x1="0" y1="74" x2="94" y2="25"/>
      <line x1="0" y1="78" x2="94" y2="81"/>
      <line x1="0" y1="82" x2="94" y2="137"/>
    </g>
  </svg>
  <div class="thumb thumb-1" role="img" aria-label="Rainbow trout close-up"></div>
  <div class="thumb thumb-2" role="img" aria-label="Fly line casting over water"></div>
  <div class="thumb thumb-3" role="img" aria-label="Assorted trout flies"></div>
</div>

<footer class="site-footer">Copyright 2014 © Cedar Hollow, All Rights Reserved</footer>

</body>
</html>
```